Hardwood Flooring Company needs packaging design

We need a packaging design for our new product. We manufacture wood flooring and this year we are launching a new product that is high quality and superior durability and we want a design that communicate the superior quality of our product. We would like to see a nice design with colors shapes that communicates quality and fashion. The product carries warranty, so we need something like a 30 year warranty stamp on the box. Measurements of the box are 4” high (100mm) X 10” wide (250mm) x 84” long (2100mm).

Flooring

• 30 Year warranty stamp
• colors like blue or purple

```html
<!DOCTYPE html>
<html lang="en">
<head>
<meta charset="utf-8">
<title>Timbra Wood Flooring – Box Packaging</title>
<link rel="stylesheet" href="https://fonts.googleapis.com/css2?family=Archivo+Black&family=Montserrat:wght@800&display=swap">
<style>
  :root {
    --paper: #ffffff;
    --dieline: #2e2a27;
    --wood-dark: #a8703f;
    --wood-mid: #c38d58;
    --wood-light: #dbcfb8;
    --wood-light-2: #cfc2a8;
    --stripe: #fff4cf;
    --brand-orange: #ea7a22;
    --label-cream: #fbf2d4;
    --label-edge: #6b4526;
    --seal-dark: #2b2b2b;
    --seal-ring: #e9e9e9;
  }
  html, body {
    margin: 0;
    padding: 0;
    width: 1200px;
    height: 4054px;
    overflow: hidden;
    background: var(--paper);
  }
  .box-net {
    position: relative;
    width: 1200px;
    height: 4054px;
    overflow: hidden;
    background: var(--paper);
  }
  .box-net__art {
    position: absolute;
    inset: 0;
  }
  .product-label {
    position: absolute;
    left: 110px;
    top: 400px;
    margin: 0;
    writing-mode: vertical-rl;
    font-family: "Montserrat", sans-serif;
    font-weight: 800;
    font-size: 92px;
    line-height: 1.02;
    letter-spacing: 4px;
    color: var(--label-cream);
    -webkit-text-stroke: 3px var(--label-edge);
    paint-order: stroke fill;
  }
  .brand-name {
    position: absolute;
    left: 100px;
    top: 1400px;
    margin: 0;
    writing-mode: vertical-rl;
    font-family: "Archivo Black", sans-serif;
    font-weight: 400;
    font-size: 250px;
    line-height: 1;
    letter-spacing: 4px;
    color: var(--brand-orange);
  }
  .warranty-seal {
    position: absolute;
    left: 104px;
    top: 3360px;
    width: 144px;
    height: 144px;
  }
</style>
</head>
<body>
<main class="box-net">
  <svg class="box-net__art" width="1200" height="4054" viewBox="0 0 1200 4054" xmlns="http://www.w3.org/2000/svg">
    <defs>
      <linearGradient id="wood-dark-fill" x1="0" y1="0" x2="1" y2="1">
        <stop offset="0" stop-color="var(--wood-dark)"/>
        <stop offset="0.5" stop-color="var(--wood-mid)"/>
        <stop offset="1" stop-color="var(--wood-dark)"/>
      </linearGradient>
      <linearGradient id="wood-light-fill" x1="0" y1="0" x2="1" y2="1">
        <stop offset="0" stop-color="var(--wood-light)"/>
        <stop offset="1" stop-color="var(--wood-light-2)"/>
      </linearGradient>
      <filter id="soft-shadow" x="-10%" y="-50%" width="120%" height="200%">
        <feGaussianBlur stdDeviation="22"/>
      </filter>
    </defs>

    <!-- top flaps -->
    <g class="flaps flaps--top" fill="var(--paper)" stroke="var(--dieline)" stroke-width="3">
      <rect x="600" y="2" width="432" height="300" rx="40"/>
      <polygon points="432,251 432,135 600,86 600,251"/>
      <polygon points="1032,251 1032,86 1200,135 1200,251"/>
    </g>
    <!-- bottom flaps -->
    <g class="flaps flaps--bottom" fill="var(--paper)" stroke="var(--dieline)" stroke-width="3">
      <rect x="600" y="3752" width="432" height="300" rx="40"/>
      <polygon points="432,3803 432,3919 600,3968 600,3803"/>
      <polygon points="1032,3803 1032,3968 1200,3919 1200,3803"/>
    </g>

    <!-- main panel artwork -->
    <g class="panel">
      <rect x="0" y="251" width="1200" height="3546" fill="url(#wood-light-fill)" role="img" aria-label="Pale wood plank floor photograph"/>
      <polygon class="panel__shadow" points="0,1150 1200,880 1200,950 0,1225" fill="#6f665a" opacity="0.55" filter="url(#soft-shadow)"/>
      <polygon class="panel__shadow" points="0,3150 1200,2920 1200,2880 0,3105" fill="#6f665a" opacity="0.55" filter="url(#soft-shadow)"/>
      <polygon points="0,251 1200,251 1200,865 0,1135" fill="url(#wood-dark-fill)" role="img" aria-label="Warm honey wood plank photograph"/>
      <polygon points="0,3149 1200,2919 1200,3797 0,3797" fill="url(#wood-dark-fill)" role="img" aria-label="Warm honey wood plank photograph"/>
      <polygon class="panel__stripe" points="0,1135 1200,865 1200,887 0,1157" fill="var(--stripe)"/>
      <polygon class="panel__stripe" points="0,3127 1200,2897 1200,2919 0,3149" fill="var(--stripe)"/>
    </g>

    <!-- panel outline and folds -->
    <g class="dieline" fill="none" stroke="var(--dieline)" stroke-width="3">
      <rect x="1.5" y="251" width="1197" height="3546"/>
      <line x1="432" y1="251" x2="432" y2="3797"/>
      <line x1="600" y1="251" x2="600" y2="3797"/>
      <line x1="1032" y1="251" x2="1032" y2="3797"/>
    </g>
  </svg>

  <h2 class="product-label">WOOD<br>FLOORING</h2>
  <h1 class="brand-name">TIMBRA</h1>

  <svg class="warranty-seal" viewBox="0 0 144 144" xmlns="http://www.w3.org/2000/svg" aria-label="30 year warranty seal">
    <circle cx="72" cy="72" r="70" fill="var(--seal-dark)"/>
    <circle cx="72" cy="72" r="60" fill="var(--seal-ring)"/>
    <circle cx="72" cy="72" r="52" fill="var(--seal-dark)"/>
    <g transform="rotate(90 72 72)" fill="#ffffff" font-family="Montserrat, sans-serif" font-weight="800" text-anchor="middle">
      <text x="72" y="64" font-size="20">30 YEAR</text>
      <text x="72" y="86" font-size="15">WARRANTY</text>
      <text x="72" y="104" font-size="12">★ ★ ★</text>
    </g>
  </svg>
</main>
</body>
</html>
```